GLOOMFEST BASH 2014 - Halloween Party

I need a 8.5x11 poster that can also be a jpeg for facebook and run as a display ad in print. I would like a facebook cover and profile picture that matches the poster. This is our 8th annual Halloween costume party and is our biggest event of the year.

Copy is as follows: (no particular order

8th Annual GLOOMFEST BASH
Halloween Costume Party
FRIDAY October 31st (need to emphasize date, usually I do it on Saturday.)
$400 in CASH PRIZES awarded at 9pm AND Midnight
DJ 7pm-2am in the tavern
Live music by RIVET PARADE in the back room. 9pm.
Drink Specials, Munchies
$5 cover in advance, $10 at the door.
Birchfield Corner Inn, 1184 County Route 41, Hillsdale, NY

Target Market(s)

We are a bar and we have live music and a DJ for this party and are awarding for prizes for the best costumes (and other costumer categories.)

Industry/Entity Type

House

Font styles to use
Other font styles liked:
• halloween, spooky but readable

Requirements
Must have
• Must communicate the details clearly, be able to read from a distance. Due to the amount of Information we need to convey, I am willng to go 8x14 poster size. The emphasis should really be on "Gloomfest Bash". "8th annual" is not very important and should be weighted less than Gloomfest Bash.
Should not have
• shouldn't be too scary. I've had shop owners tell me that some are too scary to hang in their stores.

```html
<!DOCTYPE html>
<html lang="en">
<head>
<meta charset="utf-8">
<title>Gloomfest Bash – 8th Annual Halloween Costume Party</title>
<link rel="stylesheet" href="https://fonts.googleapis.com/css2?family=Creepster&family=Metal+Mania&display=swap">
<style>
  :root {
    --pumpkin: #f39a2a;
    --pumpkin-deep: #e0781c;
    --pumpkin-light: #f7b04a;
    --moon: #ec8a2c;
    --ink: #0d0b0a;
  }
  * { margin: 0; padding: 0; box-sizing: border-box; }
  html, body { width: 929px; height: 1200px; overflow: hidden; background: var(--ink); }
  .poster {
    position: relative; width: 929px; height: 1200px; overflow: hidden;
    background: radial-gradient(ellipse at 50% 40%, var(--pumpkin-light) 0%, var(--pumpkin) 55%, var(--pumpkin-deep) 100%);
    color: var(--ink);
    font-family: "Creepster", "Metal Mania", fantasy;
  }
  .frame {
    position: absolute; inset: 0; pointer-events: none;
    border: 14px solid var(--ink);
  }
  .abs { position: absolute; white-space: nowrap; }
  .title { font-family: "Creepster", fantasy; letter-spacing: 4px; line-height: 1; }
  .title-top { left: 0; width: 929px; text-align: center; top: 88px; font-size: 150px; }
  .title-bottom { left: 78px; top: 220px; font-size: 150px; }
  .rule { position: absolute; height: 3px; background: var(--ink); }
  .annual { left: 548px; top: 268px; font-size: 54px; letter-spacing: 2px; font-family: "Creepster", fantasy; }
  .party { left: 0; width: 929px; text-align: center; top: 392px; font-size: 56px; letter-spacing: 2px; }
  .date-band {
    position: absolute; left: 0; top: 488px; width: 929px; height: 172px;
    background: var(--ink); color: var(--pumpkin); text-align: center;
  }
  .date { display: block; padding-top: 20px; font-size: 82px; letter-spacing: 3px; line-height: 1; }
  .venue { display: block; margin-top: 16px; font-family: "Metal Mania", fantasy; font-size: 23px; letter-spacing: 1px; }
  .prize-amount { left: 82px; top: 680px; font-size: 168px; line-height: 1; letter-spacing: 2px; }
  .prize-label { left: 440px; top: 716px; font-size: 52px; letter-spacing: 2px; line-height: 1; }
  .prize-time { left: 442px; top: 776px; font-family: "Metal Mania", fantasy; font-size: 24px; letter-spacing: 1px; }
  .scene { position: absolute; left: 0; top: 800px; width: 929px; height: 400px; }
  .details { left: 0; width: 1040px; text-align: center; line-height: 1.25; }
  .dj { top: 864px; font-size: 38px; letter-spacing: 1px; }
  .extras { top: 912px; font-family: "Metal Mania", fantasy; font-size: 23px; }
  .cover {
    left: 0; width: 929px; text-align: center; top: 1140px;
    font-size: 44px; letter-spacing: 1px; color: var(--pumpkin);
  }
</style>
</head>
<body>
<main class="poster">
  <svg class="scene" viewBox="0 0 929 400" role="img" aria-label="Orange harvest moon behind a hillside silhouette with a haunted house and costumed party-goers">
    <defs>
      <radialGradient id="moonGlow" cx="0.5" cy="0.5" r="0.5">
        <stop offset="0" stop-color="#ee8d2e"/>
        <stop offset="1" stop-color="#e9822a" stop-opacity="0.6"/>
      </radialGradient>
    </defs>
    <circle cx="725" cy="140" r="205" fill="url(#moonGlow)"/>
    <path d="M0 250 C 200 235, 450 245, 929 250 L 929 400 L 0 400 Z" fill="#0d0b0a"/>
  </svg>

  <h1 class="abs title title-top">GLOOMFEST</h1>
  <div class="abs title title-bottom">BASH</div>
  <span class="rule" style="left:548px; top:247px; width:312px;"></span>
  <p class="abs annual">8TH ANNUAL</p>
  <span class="rule" style="left:548px; top:345px; width:312px;"></span>
  <h2 class="abs party">HALLOWEEN COSTUME PARTY</h2>

  <section class="date-band">
    <span class="date">FRIDAY OCTOBER 31ST</span>
    <span class="venue">BIRCHFIELD CORNER INN, 1184 COUNTY ROUTE 41, HILLSDALE, NY</span>
  </section>

  <span class="rule" style="left:440px; top:702px; width:440px;"></span>
  <p class="abs title prize-amount">$400</p>
  <p class="abs prize-label">IN CASH PRIZES</p>
  <p class="abs prize-time">AWARDED AT 9PM AND MIDNIGHT</p>
  <span class="rule" style="left:440px; top:810px; width:440px;"></span>

  <p class="abs details dj">DJ 7PM–2AM IN THE TAVERN</p>
  <p class="abs details extras">LIVE MUSIC BY RIVET PARADE IN THE BACK ROOM. 9PM.<br>DRINK SPECIALS, MUNCHIES</p>

  <p class="abs cover">$5 COVER IN ADVANCE, $10 AT THE DOOR.</p>
  <div class="frame"></div>
</main>
</body>
</html>
```